Tessaway Website Redesign

We have a web site called tessaway.com that is all about education/information about legal marijuana. We're looking to significantly improve the modern-ness and look/feel of the web site - and to make it look like many of the best web sites out there today.

The task will be to come up with a better design for:
- The home page: http://tessaway.com/
- The logo (see the logo at the top of each page)
- The header and footer (for all the pages)
- The vaporizer page: http://tessaway.com/collections/vaporizer
- The store map page: http://tessaway.com/pages/shop-marijuana-in-colorado-state

The output of the project will be:
- screenshots of the designs and any images needed
- PSD file

Key requirements:
- Style needs to look fresh/modern
- Especially on the vaporizers page, the key things we want to drive is conversion - getting more people to interact with the page and actually click on the links to purchase vaporizers

Note I clarified that I don't need code (HTML or CSS) for the project. I just need the designs, including images and the PSD file. Thanks.

Industry/Entity Type

Education

Font styles to use
Sans Serif

Requirements
Must have
• Must look like a modern/clean/fresh looking website design.

```html
<!DOCTYPE html>
<html lang="en">
<head>
<meta charset="utf-8">
<title>Tessaway – Shop marijuana in style</title>
<link href="https://fonts.googleapis.com/css2?family=Roboto+Condensed:wght@400;700&family=Roboto:wght@400;500&display=swap" rel="stylesheet">
<style>
:root{
  --green:#4cd964;
  --green-text:#2ebd3f;
  --dark:#111;
  --panel:#f2f2f2;
  --page:#fff;
  --topbar:#e6e6e6;
  --footer:#efefef;
  --ink:#222;
}
*{box-sizing:border-box;margin:0;padding:0}
html,body{width:799px;height:1200px;overflow:hidden}
body{position:relative;background:var(--page);font-family:"Roboto Condensed",Arial,sans-serif;color:var(--ink)}
.abs{position:absolute}
.top-stripe{left:0;top:0;width:799px;height:4px;background:var(--green)}
.share-bar{left:0;top:4px;width:799px;height:24px;background:var(--topbar)}
.share-bar .label{position:absolute;left:580px;top:6px;font-size:10px;font-weight:700}
.share-btn{position:absolute;top:4px;height:15px;border-radius:2px;font:700 9px/15px "Roboto Condensed",sans-serif;text-align:center}
.share-btn.like{left:645px;width:34px;background:#4a6aa8;color:#fff}
.share-btn.post{left:687px;width:42px;background:#dce8f2;color:#3a6f9a;border:1px solid #b7cfe0}
.brand{left:70px;top:50px;font-weight:700;font-size:34px;color:var(--green-text);letter-spacing:.5px}
.tagline{left:152px;top:88px;font-family:Roboto,sans-serif;font-size:9px;color:#222}
.ad-slot{left:271px;top:49px;width:458px;height:55px;background:#e4e4e4;border:1px solid #bfe4c2;text-align:center}
.ad-slot b{display:block;margin-top:14px;font-weight:400;font-size:14px;color:#222}
.ad-slot span{font-size:8px;color:var(--green-text)}
.nav{left:0;top:126px;width:799px;height:31px;background:var(--dark)}
.nav-line{left:0;top:157px;width:799px;height:2px;background:var(--green)}
.nav .home{position:absolute;left:70px;top:0;width:44px;height:31px;background:var(--green)}
.nav .home svg{position:absolute;left:13px;top:7px}
.nav .item{position:absolute;top:0;height:31px;line-height:31px;color:#fff;font-size:12px;text-align:center;border-right:1px solid #333}
.search{position:absolute;left:581px;top:6px;width:141px;height:19px;background:#fff;border-radius:2px}
.search svg{position:absolute;right:4px;top:3px}
.slider{left:70px;top:159px;width:659px;height:229px;border:3px solid var(--green);background:linear-gradient(160deg,#b8b3a8 0%,#c9b38d 30%,#7f8a5a 60%,#5d6a43 100%)}
.slide-arrow{position:absolute;top:100px;width:20px;height:26px;background:rgba(255,255,255,.55)}
.slide-arrow.prev{left:-3px;border-radius:0 13px 13px 0}
.slide-arrow.next{right:-3px;border-radius:13px 0 0 13px}
.section{left:70px;width:659px;background:var(--panel);border:1px solid #666;border-bottom:2px solid var(--green)}
.section-head{position:relative;height:28px;background:var(--dark)}
.section-head h2{position:absolute;left:0;top:0;height:28px;line-height:28px;padding:0 11px;background:var(--green);font-weight:400;font-size:14px;color:#111}
.view-all{position:absolute;right:4px;top:5px;height:18px;line-height:18px;padding:0 7px;background:#fff;font-size:10px;border:1px solid #ccc}
.thumb{position:absolute;top:39px;width:149px;height:100px}
.thumb-cap{position:absolute;top:114px;width:152px;font-size:10px;line-height:12.5px;margin-top:34px}
.post-img{position:absolute;left:10px;width:176px;height:111px}
.post-body{position:absolute;left:199px;width:440px}
.post-body h3{font-weight:700;font-size:17.5px;color:var(--green-text);margin-bottom:4px}
.post-body p{font-size:9.8px;line-height:14.4px;color:#222}
.footer{left:0;top:1065px;width:799px;height:108px;background:var(--footer);border-top:2px solid var(--green)}
.footer h4{position:absolute;font-weight:400;font-size:13px;top:18px}
.links{position:absolute;top:42px;list-style:none;font-family:Roboto,sans-serif;font-size:7.5px;line-height:12.6px}
.links li::before{content:"> "}
.vdiv{position:absolute;top:20px;height:66px;border-left:1px dotted #aaa}
.contact{position:absolute;left:387px;top:42px;font-family:Roboto,sans-serif;font-size:7.5px;line-height:12.6px}
.email{position:absolute;left:575px;top:67px;font-family:Roboto,sans-serif;font-size:16px}
.bottom{left:0;top:1173px;width:799px;height:27px;background:#1b1b1b}
.bottom span{position:absolute;left:70px;top:9px;font-family:Roboto,sans-serif;font-size:7.5px;color:var(--green)}
</style>
</head>
<body>
<div class="abs top-stripe"></div>
<div class="abs share-bar">
  <span class="label">Share Tessaway -</span>
  <span class="share-btn like">Like</span>
  <span class="share-btn post">Post</span>
</div>

<div class="abs brand">Tessaway</div>
<div class="abs tagline">Shop marijuana in style</div>
<div class="abs ad-slot"><b>Ad goes here</b><span>730x90</span></div>

<nav class="abs nav">
  <a class="home" aria-label="Home"><svg width="18" height="17" viewBox="0 0 18 17"><path d="M9 0 0 8h2.5v9h5v-6h3v6h5V8H18z" fill="#111"/></svg></a>
  <span class="item" style="left:116px;width:66px">BLOG</span>
  <span class="item" style="left:182px;width:119px">MARIJUANA 101</span>
  <span class="item" style="left:301px;width:133px">LEGAL MARIJUANA</span>
  <span class="item" style="left:434px;width:102px">VAPORIZERS</span>
  <div class="search"><svg width="13" height="13" viewBox="0 0 13 13"><circle cx="5" cy="5" r="3.8" fill="none" stroke="#4cd964" stroke-width="2"/><path d="M8 8l4 4" stroke="#4cd964" stroke-width="2.4"/></svg></div>
</nav>
<div class="abs nav-line"></div>

<div class="abs slider" role="img" aria-label="Gloved hands holding dried cannabis buds beside wrapped bales">
  <span class="slide-arrow prev"></span><span class="slide-arrow next"></span>
</div>

<section class="abs section" style="top:406px;height:189px">
  <div class="section-head"><h2>RECENT POST</h2><span class="view-all">View All</span></div>
  <div class="thumb" style="left:10px;background:linear-gradient(#a9c6e6,#8ea4a8 50%,#4f7a3a)" role="img" aria-label="Denver skyline over a park lake"></div>
  <div class="thumb" style="left:172px;background:linear-gradient(#9fb2c4,#c7cdd3 50%,#6c6f72)" role="img" aria-label="Seattle skyline with the Space Needle"></div>
  <div class="thumb" style="left:334px;background:linear-gradient(#3f3f3f,#6a6560 50%,#2d2a28)" role="img" aria-label="Dark burning city skyline"></div>
  <div class="thumb" style="left:498px;background:linear-gradient(135deg,#7a6a3a,#9a8f6b 50%,#5b4a2a)" role="img" aria-label="Hands holding glass jars of cannabis"></div>
  <p class="thumb-cap" style="left:10px">Map and ranking of Colorado Stores.</p>
  <p class="thumb-cap" style="left:172px">Map of Washington State stores opening in July.</p>
  <p class="thumb-cap" style="left:334px">Thousands Die As Drugs Sweep Washington State.</p>
  <p class="thumb-cap" style="left:498px">The 6 Best Ways to Store Your Weed.</p>
</section>

<section class="abs section" style="top:614px;height:418px">
  <div class="section-head"><h2>ALL POST</h2><span class="view-all">View All</span></div>
  <div class="post-img" style="top:39px;background:linear-gradient(135deg,#4a3a30,#7a6050 50%,#5a6068)" role="img" aria-label="Man smoking on a couch"></div>
  <div class="post-body" style="top:44px">
    <h3>New Colorado Springs Smoker Accepting Potential Obesity</h3>
    <p>Stating that legal marijuana is just "too damn convenient" and makes food taste "too damn good," Dale Hutchins, a 28-year-old mechanic living in Colorado Springs, Colorado, told reporters that he has accepted his fate as a potential fat man and that there's nothing he can do to stop it.</p>
  </div>
  <div class="post-img" style="top:163px;background:linear-gradient(135deg,#3a2c22,#8a6a50 45%,#d8d4cc 70%,#2a2520)" role="img" aria-label="Young man in a printed t-shirt relaxing"></div>
  <div class="post-body" style="top:168px">
    <h3>Top 7 Thoughts Everyone Has the First Time They Get High</h3>
    <p>Everyone has a unique story about the thoughts that ran through their head the first time they got high. First-timers experience highs that are more intense than any other they may ever experience in their lives, which makes those thoughts even more real, no matter how silly they may be. Here are the top 7 thoughts people have the first time they smoke weed.</p>
  </div>
  <div class="post-img" style="top:289px;background:radial-gradient(circle at 50% 45%,#e8ece4,#8a9a80 40%,#1a1e18 80%)" role="img" aria-label="Close-up of a frosty cannabis bud"></div>
  <div class="post-body" style="top:294px">
    <h3>The Greatest Strain Names (And What They Are)</h3>
    <p>Everyone has a unique story about the thoughts that ran through their head the first time they got high. First-timers experience highs that are more intense than any other they may ever experience in their lives, which makes those thoughts even more real, no matter how silly they may be. Here are the top 7 thoughts people have the first time they smoke weed.</p>
  </div>
</section>

<footer class="abs footer">
  <h4 style="left:70px">Quick Links</h4>
  <ul class="links" style="left:70px"><li>Blog</li><li>Marijuana 101</li><li>Legal Marijuana</li><li>Vaporizers</li></ul>
  <ul class="links" style="left:156px"><li>About Us</li><li>Colorado Stores</li><li>Washington State Stores</li><li>Edibles (Yummy food!)</li></ul>
  <ul class="links" style="left:263px"><li>Find friends who get high</li><li>Frequently Asked Questions</li><li>Discussion Forum</li><li>Vaporizer Rankings</li></ul>
  <span class="vdiv" style="left:370px"></span>
  <h4 style="left:387px">Contact Information</h4>
  <div class="contact">
    <div style="font-weight:500">TESSAWAY</div>
    <div>Lorem Ipsum is therefore always free from repetition</div>
    <div style="margin-top:3px"><svg width="10" height="10" viewBox="0 0 10 10" style="vertical-align:-2px"><path d="M2 0l2 2.5-1.2 1.3c.6 1.4 1.8 2.6 3.4 3.4L7.5 6 10 8l-1.5 2C4 9.8.2 6 0 1.5z" fill="#222"/></svg> +0 (000) 000-0000</div>
  </div>
  <span class="vdiv" style="left:562px"></span>
  <svg class="abs" style="left:618px;top:22px" width="64" height="35" viewBox="0 0 64 35"><rect width="64" height="35" fill="#4cd964"/><path d="M0 0l32 20L64 0M0 35l24-19M64 35L40 16" fill="none" stroke="#efefef" stroke-width="2.4"/></svg>
  <div class="email">contact@tessaway.com</div>
</footer>
<div class="abs bottom"><span>Copyright © 2014 Tessaway</span></div>
</body>
</html>
```